High end cable company busines card and letterhead

Dear designers,
We assemble high end audio cables that cost a couple of hundred dollars per piece and we are improving the looks of the product.
When people buy a cable they get a leather pouch with the invoice (letterhead) , a business card of the maker and also a quality control card  / warranty card.
The quality control card  is the same size as a business card and the back of the quality control card is the same back as the business card. So we need 4 things:
-1 back of a business card
-1 front of a business card (a file where we can change the name and details of the worker)
-1 quality control front (I will add a photo of an example)
-1 letterhead
We want to make letterpress business cards and use shiny foil for the logo’s. We like the colors black and copper or black and gold for the back. The front of the business card can also be black, copper and white but it does not have to be those colors. We want people to have the feeling that they bought something expensive and high quality.
The front of the quality control card has to be white so we can check things off with a sharpie / pen.
What has to be on the cards:
Business card:
- Our Logo
-Text: Meet the maker (people get the business card of the one who made the cable)
-Name
-Address
-Website (www.tallowfenwire.com)
-Email address
-Text: For any advise or questions about your cable feel free to contact me.
What has to be on the quality control card:
-Our logo
-Text: quality controll and warranty card (small at the bottom)
-text:
Assembled by:________________
Date: ______-______-____________
QC by:_________________________

Assembly QC [   ]
Measurement QC [   ]
Aesthetics [   ]
(The box [    ] is for the initials of the person that does the QC, it can also be a line or something else)
The letterhead can be your own idea as long as it looks luxurious.
You can download our logo. We have a black one and gold / black but you can change the Color to Match your design. (For instance copper or something) There is also a white one that can be used with the icon on the left.
Some links of stuff we like:
-https://clipvault.example/Kq3rLm8zXa1 (The looks of this card maybe a bit less busy looking)
-https://b.brindlemart.example/_pRxwQaf
-https://b.brindlemart.example/_pTj4Wob
-https://b.brindlemart.example/_pYeuZ11

```html
<!DOCTYPE html>
<html lang="en">
<head>
<meta charset="utf-8">
<title>Tallowfen Wire — Business Card</title>
<link href="https://fonts.googleapis.com/css2?family=Josefin+Sans:wght@400;600&family=Crimson+Text:ital@1&display=swap" rel="stylesheet">
<style>
  :root {
    --backdrop: #3a3532;
    --card: #1f1e1f;
    --card-edge: #d9a617;
    --gold: #d9a617;
    --white: #f2f2f2;
    --muted: #cfcfcf;
  }
  * { box-sizing: border-box; margin: 0; padding: 0; }
  html, body { width: 1200px; height: 716px; overflow: hidden; }
  body {
    background: var(--backdrop);
    font-family: "Josefin Sans", sans-serif;
    position: relative;
  }
  .card {
    position: absolute;
    top: 200px;
    width: 540px;
    height: 309px;
    background: var(--card);
    border-bottom: 3px solid var(--card-edge);
    box-shadow: 0 12px 30px rgba(0,0,0,.45);
  }
  .card--front { left: 45px; }
  .card--back { left: 615px; }

  .brand {
    position: absolute;
    left: 58px;
    top: 120px;
    display: flex;
    align-items: center;
    gap: 14px;
  }
  .brand__mark {
    width: 20px; height: 20px;
    background: var(--gold);
  }
  .brand__name {
    color: var(--gold);
    font-weight: 400;
    font-size: 30px;
    letter-spacing: 8px;
    text-transform: uppercase;
  }

  .contact {
    position: absolute;
    right: 34px;
    top: 70px;
    text-align: right;
    color: var(--white);
  }
  .contact__name {
    font-size: 22px;
    font-weight: 600;
    letter-spacing: 1px;
    text-transform: uppercase;
  }
  .contact__role {
    color: var(--gold);
    font-size: 14px;
    margin-top: 2px;
  }
  .divider {
    display: inline-block;
    width: 46px;
    height: 1px;
    background: var(--white);
    margin: 12px 0 10px;
  }
  .contact__list { list-style: none; font-size: 13px; line-height: 1.35; color: var(--muted); }
  .contact__list li { display: flex; justify-content: flex-end; align-items: center; gap: 10px; }
  .contact__list .text { text-align: right; }
  .icon { width: 12px; height: 12px; flex: none; }
  .icon--blank { width: 12px; }
  .contact__note {
    font-family: "Crimson Text", serif;
    font-style: italic;
    color: var(--gold);
    font-size: 15px;
    line-height: 1.2;
    margin-top: 2px;
  }
</style>
</head>
<body>
  <section class="card card--front" aria-label="Business card front">
    <div class="brand">
      <span class="brand__mark"></span>
      <span class="brand__name">Tallowfen Wire</span>
    </div>
  </section>

  <section class="card card--back" aria-label="Business card back">
    <div class="contact">
      <h1 class="contact__name">Daniel Hart</h1>
      <p class="contact__role">President</p>
      <span class="divider"></span>
      <ul class="contact__list">
        <li><span class="text">2140 Alder Row</span><span class="icon--blank"></span></li>
        <li><span class="text">Juneau, Alaska 99801</span>
          <svg class="icon" viewBox="0 0 12 12" fill="none" stroke="#d9a617" stroke-width="1"><path d="M6 11 C3 7 2 5.5 2 4.2 A4 4 0 0 1 10 4.2 C10 5.5 9 7 6 11Z"/><circle cx="6" cy="4.3" r="1.4"/></svg></li>
        <li><span class="text">555-214-0873</span>
          <svg class="icon" viewBox="0 0 12 12" fill="none" stroke="#d9a617" stroke-width="1"><path d="M2.5 1.5 L4.5 1.5 L5.3 4 L4 5 C4.8 6.7 5.5 7.3 7 8 L8 6.7 L10.5 7.5 L10.5 9.5 C6 10 2 6 2.5 1.5Z"/></svg></li>
        <li><span class="text">info@tallowfenwire.com</span>
          <svg class="icon" viewBox="0 0 12 12" fill="none" stroke="#d9a617" stroke-width="1"><rect x="1" y="2.5" width="10" height="7"/><path d="M1 2.5 L6 6.5 L11 2.5"/></svg></li>
        <li><span class="text">tallowfenwire.com</span>
          <svg class="icon" viewBox="0 0 12 12" fill="none" stroke="#d9a617" stroke-width="1"><circle cx="6" cy="6" r="5"/><path d="M1 6 H11 M6 1 C3.5 3.5 3.5 8.5 6 11 M6 1 C8.5 3.5 8.5 8.5 6 11"/></svg></li>
      </ul>
      <span class="divider"></span>
      <p class="contact__note">For any advise or questions about<br>your cable feel free to contact me.</p>
    </div>
  </section>
</body>
</html>
```